Build a Web page - Dovin Pratchell Homes, LLC - a custom home builder

We are a custom home builder in Wisconsin. Need a basic web page with a home page, About Us, Contact info, Gallery, and Testimonials page. Gallery will probably have sub-pages and each will have about ten pictures or less. I already own the domain and have web hosting through Wix, I just need the site built. Once the page is built I should be able to do the upkeep on it myself. If I need to add pictures or whatever.
Updates

Project Deadline Extended
Reason: I am still looking through designs and will select soon - thank you!

Target Market(s)

Gen X and Millennials who are looking to build a home. Custom built homes - not generic spec homes.

Industry/Entity Type

Home Builder

Number of Pages Required

5+ page

Font styles to use
Sans Serif

Colors
ffffff
ec1f27
000000
9d9d9d

Requirements
Must have
• I have no idea if I want coded or in coded. I'm not sure of the difference and why I would want one over the other.
Nice to have
• We like the following colors - red, black, gray, white.
Should not have
• not a big fan of clip art like hammers, tape measures, etc. Must look professional.

```html
<!DOCTYPE html>
<html lang="en">
<head>
<meta charset="utf-8">
<title>Dovin Pratchell Homes, LLC</title>
<link rel="stylesheet" href="https://fonts.googleapis.com/css2?family=Poppins:wght@400;500;600;700&family=Open+Sans:wght@400;600;700&display=swap">
<style>
:root{
  --red:#a81c21;
  --red-bright:#c62128;
  --black:#151415;
  --ink:#1b1b1b;
  --grey:#9d9d9d;
  --text:#6c6c6c;
  --light:#f6f6f6;
  --white:#ffffff;
  --star:#f39c12;
}
*{box-sizing:border-box;margin:0;padding:0}
html,body{width:1200px;height:2711px;overflow:hidden}
body{position:relative;background:var(--white);font-family:"Open Sans",Arial,sans-serif;color:var(--ink)}
.abs{position:absolute}
.heading{font-family:"Poppins",Arial,sans-serif}

/* hero */
.hero{left:0;top:0;width:1200px;height:623px;overflow:hidden}
.hero-photo{position:absolute;inset:0;background:linear-gradient(180deg,#3d5676 0%,#6e84a0 22%,#8a8f86 38%,#5d6a4c 52%,#4c6a2c 68%,#3e6122 100%)}
.hero-shade{position:absolute;inset:0;background:rgba(0,0,0,.22)}
.brand{left:99px;top:30px;display:flex;align-items:center;gap:12px;color:var(--white);font-family:"Poppins",sans-serif;font-weight:600;font-size:15px;letter-spacing:1px}
.brand-mark{width:34px;height:34px;background:var(--red)}
.nav{right:88px;top:38px;display:flex;gap:38px;list-style:none}
.nav li{color:var(--white);font-family:"Poppins",sans-serif;font-weight:500;font-size:12.5px;letter-spacing:.3px}
.hero-frame{left:466px;top:186px;width:266px;height:251px;border:2px solid rgba(255,255,255,.9)}
.hero-kicker{left:0;width:1200px;top:234px;text-align:center;color:var(--white);font-family:"Poppins",sans-serif;font-weight:600;font-size:16px}
.hero-title{left:0;width:1200px;top:252px;text-align:center;color:var(--white);font-family:"Poppins",sans-serif;font-weight:600;font-size:52px;letter-spacing:.5px;line-height:74px}
.hero-btn{left:537px;top:336px;width:128px;height:47px;background:var(--white);color:var(--ink);font-family:"Poppins",sans-serif;font-weight:600;font-size:11.5px;display:flex;align-items:center;justify-content:center}
.slide-arrow{width:34px;height:34px;border-radius:50%;display:flex;align-items:center;justify-content:center}
.slide-prev{left:32px;top:292px;background:rgba(255,255,255,.25)}
.slide-next{left:1136px;top:292px;background:var(--white)}
.mouse{left:591px;top:562px}

/* about */
.side-label{left:-52px;top:850px;transform:rotate(-90deg);font-family:"Poppins",sans-serif;font-weight:700;font-size:58px;color:#f1f1f1;letter-spacing:4px;width:300px;text-align:center}
.about-photo{left:88px;top:699px;width:467px;height:349px;background:linear-gradient(180deg,#d9d6c9 0%,#cfcab8 45%,#8a3b33 62%,#7a6b4e 85%,#5f7d3a 100%)}
.about-rule{left:555px;top:762px;width:47px;height:1px;background:var(--red)}
.about-dot{left:598px;top:759px;width:7px;height:7px;border-radius:50%;background:var(--red)}
.about-title{left:632px;top:746px;font-size:28px;font-weight:500;color:var(--ink)}
.about-copy{left:632px;top:797px;width:480px;font-size:12.5px;line-height:22px;color:var(--text)}
.about-copy p+p{margin-top:20px}
.btn-outline{left:632px;top:952px;width:132px;height:44px;border:2px solid var(--red);color:var(--red);font-family:"Poppins",sans-serif;font-weight:600;font-size:11px;display:flex;align-items:center;justify-content:center}

/* gallery */
.gallery{left:0;top:1138px;width:1200px;height:669px;background:var(--light)}
.section-title{left:0;width:1200px;text-align:center;font-size:26px;font-weight:600;color:var(--ink)}
.view-all{left:1061px;top:1216px;font-family:"Poppins",sans-serif;font-size:11px;font-weight:600;color:var(--red);text-decoration:underline}
.tile{width:246px;height:230px}
.tile-hover{background:linear-gradient(180deg,#b12a2c,#a02226);display:flex;flex-direction:column;align-items:center;justify-content:center}
.tile-hover-frame{position:absolute;left:14px;top:14px;right:14px;bottom:14px;border:1px solid rgba(255,255,255,.6)}
.tile-search{width:42px;height:42px;border-radius:50%;background:var(--white);display:flex;align-items:center;justify-content:center;margin-bottom:14px}
.tile-caption{color:var(--white);font-family:"Poppins",sans-serif;font-weight:600;font-size:12px}

/* testimonial */
.stars{left:0;width:1200px;top:1942px;text-align:center;color:var(--star);font-size:15px;letter-spacing:3px}
.quote-mark{font-family:"Poppins",sans-serif;font-size:80px;font-weight:700;color:#e3e3e3;line-height:1}
.quote-text{left:240px;top:1976px;width:721px;text-align:center;font-size:13px;line-height:23px;color:var(--text)}
.avatar{left:569px;top:2040px;width:62px;height:62px;border-radius:50%;background:radial-gradient(circle,#8a7764,#3a3330)}
.avatar-rule{left:452px;top:2071px;width:108px;height:1px;background:#eaeaea}
.client-name{left:647px;top:2050px;font-family:"Poppins",sans-serif;font-weight:600;font-size:15px;letter-spacing:1px}
.client-role{left:647px;top:2073px;font-size:11px;color:var(--grey)}
.pager{left:1060px;font-size:11px;color:var(--ink);display:flex;align-items:center;gap:10px}
.pager span.line{display:block;width:28px;height:1px;background:var(--ink)}
.pager.active{color:var(--red)}
.pager.active span.line{background:var(--red)}

/* newsletter */
.newsletter{left:0;top:2174px;width:1200px;height:170px;background:var(--red)}
.news-kicker{left:88px;top:2231px;color:var(--white);font-family:"Poppins",sans-serif;font-weight:500;font-size:13px}
.news-title{left:88px;top:2252px;color:var(--white);font-family:"Poppins",sans-serif;font-weight:600;font-size:30px}
.news-input{left:502px;top:2233px;width:490px;height:53px;background:var(--white);display:flex;align-items:center;padding-left:18px;gap:8px;font-size:11px;color:#777}
.news-btn{left:992px;top:2233px;width:118px;height:53px;background:var(--black);color:var(--white);font-family:"Poppins",sans-serif;font-weight:600;font-size:12px;display:flex;align-items:center;justify-content:center}

/* footer */
.footer{left:0;top:2344px;width:1200px;height:367px;background:var(--black)}
.foot-head{top:2412px;color:var(--white);font-family:"Poppins",sans-serif;font-weight:500;font-size:13.5px;letter-spacing:.3px}
.foot-divider{top:2403px;width:1px;height:199px;background:#2a2a2a}
.foot-links{list-style:none;color:#b9b9b9;font-size:11.5px}
.foot-links li{height:31px;display:flex;align-items:flex-start;gap:8px}
.foot-links li::before{content:"›";color:var(--red-bright)}
.contact-label{color:var(--white);font-weight:700;font-size:11.5px}
.contact-line{color:#b9b9b9;font-size:11.5px;line-height:20px;display:flex;gap:10px}
.social{list-style:none;left:1021px;top:2447px}
.social li{display:flex;align-items:center;gap:9px;height:38px;color:#b9b9b9;font-size:11.5px}
.social .dot{width:26px;height:26px;border-radius:50%}
.foot-rule{left:88px;top:2656px;width:1022px;height:1px;background:#2e2e2e}
.copyright{left:0;width:1200px;top:2674px;text-align:center;color:var(--white);font-size:11.5px}
.to-top{left:1137px;top:2644px;width:32px;height:32px;border-radius:50%;background:var(--red-bright);display:flex;align-items:center;justify-content:center}
</style>
</head>
<body>

<!-- Hero -->
<section class="hero abs">
  <div class="hero-photo" role="img" aria-label="Photo of a two-storey custom home with green siding on a wide lawn under a blue sky"></div>
  <div class="hero-shade"></div>
</section>
<div class="brand abs"><span class="brand-mark"></span>DOVIN PRATCHELL HOMES</div>
<ul class="nav abs">
  <li>HOME</li><li>ABOUT US</li><li>GALLERY</li><li>TESTIMONIALS</li><li>CONTACT INFO</li>
</ul>
<div class="hero-frame abs"></div>
<div class="hero-kicker abs">WELCOME TO</div>
<h1 class="hero-title abs">DOVIN PRATCHELL HOMES</h1>
<div class="hero-btn abs">GET STARTED</div>
<div class="slide-arrow slide-prev abs"><svg width="10" height="10" viewBox="0 0 10 10"><path d="M6.5 1.5 3 5l3.5 3.5" fill="none" stroke="#fff" stroke-width="1.6"/></svg></div>
<div class="slide-arrow slide-next abs"><svg width="10" height="10" viewBox="0 0 10 10"><path d="M3.5 1.5 7 5 3.5 8.5" fill="none" stroke="#222" stroke-width="1.6"/></svg></div>
<svg class="mouse abs" width="20" height="34" viewBox="0 0 20 34"><rect x="1.5" y="1.5" width="17" height="31" rx="8.5" fill="none" stroke="#fff" stroke-width="2"/><line x1="10" y1="8" x2="10" y2="14" stroke="#fff" stroke-width="2"/></svg>

<!-- About -->
<div class="side-label abs">SHORT INFO</div>
<div class="about-photo abs" role="img" aria-label="Photo of a red wooden backyard deck with patio furniture behind a house"></div>
<div class="about-rule abs"></div>
<div class="about-dot abs"></div>
<h2 class="about-title heading abs">ABOUT US</h2>
<div class="about-copy abs">
  <p>Aenean sollicitudin, lorem quis bibendum auctor, nisi elit consequat ipsum, nec sagittis sem nibh id elit. Duis sed odio sit amet nibh vulputate cursus a sit amet mauris morbi accumsan [...]</p>
  <p>Mauris in erat justo. Nullam ac urna eu felis dapibus condimentum sit amet a augue. Sed non neque elit. Sed ut imperdiet nisi [...]</p>
</div>
<div class="btn-outline abs">LEARN MORE</div>

<!-- Gallery -->
<section class="gallery abs"></section>
<h2 class="section-title heading abs" style="top:1201px">OUR GALLERY</h2>
<div class="view-all abs">VIEW ALL</div>
<div class="tile abs" style="left:88px;top:1265px;background:linear-gradient(180deg,#dcdcdc 0%,#c9c6c0 45%,#8b6f5a 58%,#4f7a32 75%,#3d6a25 100%)" role="img" aria-label="Photo of a ranch home with a front lawn"></div>
<div class="tile abs" style="left:347px;top:1265px;background:linear-gradient(180deg,#cdbfae,#b9a791 60%,#a8957e)" role="img" aria-label="Photo of a tiled walk-in shower with a bench"></div>
<div class="tile abs" style="left:605px;top:1265px;background:linear-gradient(180deg,#e2e2e4,#cfcfd2 60%,#8a5a34 85%,#7a4c2c)" role="img" aria-label="Photo of a hallway with wood flooring"></div>
<div class="tile tile-hover abs" style="left:864px;top:1265px" role="img" aria-label="Photo of a bedroom shown under a red hover overlay">
  <div class="tile-hover-frame"></div>
  <div class="tile-search"><svg width="14" height="14" viewBox="0 0 14 14"><circle cx="6" cy="6" r="4.2" fill="none" stroke="#a81c21" stroke-width="1.8"/><line x1="9" y1="9" x2="12.5" y2="12.5" stroke="#a81c21" stroke-width="1.8"/></svg></div>
  <div class="tile-caption">SOME HEADING GOES HERE</div>
</div>
<div class="tile abs" style="left:88px;top:1507px;background:linear-gradient(180deg,#d9d8d3,#c7c4bb 60%,#b7ad9b)" role="img" aria-label="Photo of a bathroom with white vanity"></div>
<div class="tile abs" style="left:347px;top:1507px;background:linear-gradient(180deg,#e4e1dc,#cdbfb0 40%,#8a4a2a 70%,#b9ad9c)" role="img" aria-label="Photo of a wooden staircase with railing"></div>
<div class="tile abs" style="left:605px;top:1507px;background:linear-gradient(180deg,#d8d4ca,#a99a88 45%,#6a3c2c 75%,#8f7f6e)" role="img" aria-label="Photo of a finished basement family room"></div>
<div class="tile abs" style="left:864px;top:1507px;background:linear-gradient(180deg,#e7e8ea 0%,#c9c4b8 40%,#3f6d2a 65%,#4a7e2c 100%)" role="img" aria-label="Photo of a home with a stone patio and garden"></div>

<!-- Testimonial -->
<h2 class="section-title heading abs" style="top:1872px">CLIENT'S TESTOMONIAL</h2>
<div class="stars abs">★★★★★</div>
<div class="quote-mark abs" style="left:190px;top:1950px">“</div>
<div class="quote-mark abs" style="left:792px;top:1992px">”</div>
<p class="quote-text abs">Curabitur ullamcorper ultricies nisi nam eget dui etiam rhoncus maecenas tempus tellus eget condimentum rhoncus sem quam semper libero, sit amet adipiscing sem neque sed ipsum.</p>
<div class="avatar-rule abs"></div>
<div class="avatar abs" role="img" aria-label="Client portrait"></div>
<div class="client-name abs">Wren</div>
<div class="client-role abs">Monthly Subscriber</div>
<div class="pager abs" style="top:1962px">1<span class="line"></span></div>
<div class="pager active abs" style="top:1985px">2<span class="line"></span><svg class="abs" style="left:99px;top:3px" width="10" height="10"><circle cx="5" cy="5" r="4.5" fill="#a81c21"/></svg></div>
<div class="pager abs" style="top:2005px">3<span class="line"></span></div>

<!-- Newsletter -->
<section class="newsletter abs"></section>
<div class="news-kicker abs">LATEST NEWS &amp; DEALS</div>
<h2 class="news-title abs">NEWSLETTER SIGNUP</h2>
<div class="news-input abs"><svg width="12" height="9" viewBox="0 0 12 9"><rect x=".5" y=".5" width="11" height="8" fill="none" stroke="#999"/><path d="M.5.5 6 5l5.5-4.5" fill="none" stroke="#999"/></svg>Enter Your Email Address</div>
<div class="news-btn abs">SUBSCRIBE</div>

<!-- Footer -->
<footer class="footer abs"></footer>
<div class="foot-head abs" style="left:88px">QUICK LINKS</div>
<div class="foot-head abs" style="left:340px">INFORMATION</div>
<div class="foot-head abs" style="left:650px">CONTACT INFO</div>
<div class="foot-head abs" style="left:1021px">FOLLOW US</div>
<div class="foot-divider abs" style="left:253px"></div>
<div class="foot-divider abs" style="left:542px"></div>
<div class="foot-divider abs" style="left:913px"></div>
<ul class="foot-links abs" style="left:88px;top:2450px"><li>Home</li><li>About Us</li><li>Gallery</li><li>Testimonial</li></ul>
<ul class="foot-links abs" style="left:340px;top:2450px"><li>About</li><li>Services</li><li>Terms &amp; Conditions</li><li>Privacy Policy</li></ul>
<div class="contact-label abs" style="left:650px;top:2450px">Location</div>
<div class="contact-line abs" style="left:650px;top:2470px">
  <svg width="11" height="9" viewBox="0 0 11 9" style="margin-top:6px"><rect width="11" height="9" fill="#c62128"/></svg>
  <span>Some address line goes here,<br>cit,name country name</span>
</div>
<div class="contact-label abs" style="left:650px;top:2532px">Phone number:</div>
<div class="contact-line abs" style="left:650px;top:2552px">
  <svg width="11" height="11" viewBox="0 0 11 11" style="margin-top:5px"><path d="M2 1h2l1 2.5-1.3 1a6 6 0 0 0 2.8 2.8l1-1.3L10 7v2a1 1 0 0 1-1 1A8 8 0 0 1 1 2a1 1 0 0 1 1-1z" fill="#c62128"/></svg>
  <span>(123) 456 7890</span>
</div>
<ul class="social abs">
  <li><span class="dot" style="background:#3b5998"></span>Friendloop</li>
  <li><span class="dot" style="background:#1da1f2"></span>Chirpline</li>
  <li><span class="dot" style="background:#d73d32"></span>Searchly</li>
  <li><span class="dot" style="background:#1a6a9a"></span>Workwire</li>
</ul>
<div class="foot-rule abs"></div>
<div class="copyright abs">© 2017, All Rights Reserved.</div>
<div class="to-top abs"><svg width="10" height="8" viewBox="0 0 10 8"><path d="M1 6.5 5 2.5l4 4" fill="none" stroke="#fff" stroke-width="1.6"/></svg></div>

</body>
</html>
```